Website Design for Satellite Data/HighTech Company

Please read the full description of what we want here:
https://files.brivantodocs.net/sheet/d/7QpwLx3Kv-Tn9eRbuM2fHc0JsYd4aWkZ8oNe-q5tVrBu/view?mode=share
We want a nice landing page/static website for the company. Modern and attractive, visually oriented with illustrations where pertinent. It should be static, in other words not based on wordpress or any other system, just HTML files using CSS and javascript. We should be able to just open it from the disk in our laptop with a browser and see it.
Target Market(s)
AgriTech
Industry/Entity Type
AgriTech
Coding
Coded - Design and coding required
Number of Pages Required
3 page
Look and feel
Each slider illustrates characteristics of the customer's brand and the style your logo design should communicate.

```html
<!DOCTYPE html>
<html lang="en">
<head>
<meta charset="utf-8">
<title>Terravia — Earth &amp; Space Data</title>
<link rel="stylesheet" href="https://fonts.googleapis.com/css2?family=Montserrat:wght@500;600;700;800&family=Lato:wght@400;700&display=swap">
<style>
:root{
  --navy:#2b4672;
  --navy-dark:#213a63;
  --ink:#1d1d1f;
  --text:#3a3a3a;
  --white:#ffffff;
  --light:#f1f1f3;
  --grey:#e1e2e6;
  --space:#05070c;
  --icon-bg:#e9ecf2;
}
*{box-sizing:border-box;margin:0;padding:0}
html,body{width:1200px;height:4158px;overflow:hidden}
body{font-family:"Lato",Arial,sans-serif;color:var(--text);background:var(--white);position:relative}
section,header,footer{position:relative;width:1200px;overflow:hidden}
h1,h2,h3{font-family:"Montserrat",Arial,sans-serif}
.btn{display:inline-block;background:var(--navy);color:var(--white);font-family:"Montserrat",Arial,sans-serif;font-weight:700;font-size:11px;padding:10px 17px;letter-spacing:.2px}
.btn-light{background:var(--white);color:var(--ink)}
.rule{width:74px;height:2px;background:var(--navy);margin:0 auto}
.brand{display:flex;align-items:center;gap:10px;font-family:"Montserrat",Arial,sans-serif;font-weight:700;color:var(--white);letter-spacing:3px}
.brand-dot{width:18px;height:18px;border-radius:50%;background:var(--white)}

/* Hero */
.hero{height:690px;background:radial-gradient(ellipse at 55% 45%,#4d5e55 0%,#37453e 45%,#222b2b 100%)}
.hero .brand{position:absolute;left:128px;top:60px;font-size:30px}
.nav{position:absolute;top:26px;left:386px;display:flex;align-items:center;gap:6px;font-family:"Montserrat",Arial,sans-serif;font-weight:700;font-size:13px;color:var(--white)}
.nav a{padding:6px 8px}
.nav a + a{margin-left:8px}
.nav .active{background:var(--navy)}
.lang{margin-left:14px;border:1.5px solid var(--white);padding:6px 12px;width:66px;display:flex;justify-content:space-between}
.hero h1{position:absolute;top:250px;width:100%;text-align:center;color:var(--white);font-size:48px;font-weight:800;line-height:58px}
.hero .tag{position:absolute;top:386px;width:100%;text-align:center;color:var(--white);font-family:"Montserrat",Arial,sans-serif;font-weight:700;font-size:17px}
.dots{position:absolute;top:643px;left:568px;display:flex;gap:5px}
.dots span{width:8px;height:8px;background:var(--white)}
.dots span.on{background:transparent;border:1.5px solid var(--white)}

/* About */
.about{height:512px;background:var(--space)}
.about-visual{position:absolute;right:0;top:0;width:600px;height:512px;background:radial-gradient(circle at 95% 60%,#3d6fa8 0%,#163052 35%,#05070c 70%)}
.about-copy{position:absolute;left:128px;top:44px;width:472px;color:var(--white)}
.about h2{font-size:21px;font-weight:700}
.about .line{width:74px;height:1.5px;background:var(--white);margin:18px 0 20px}
.about p{font-size:14.5px;line-height:20px;text-align:justify;margin-bottom:20px}

/* Services */
.services{height:362px;text-align:center}
.services h2{padding-top:44px;font-size:20px;color:var(--ink)}
.services .sub{font-size:14px;margin:10px 0 30px;color:var(--ink)}
.service-list{display:flex;justify-content:space-between;width:816px;margin:52px auto 0}
.service{width:160px;font-size:13.5px;line-height:20px;color:var(--ink)}
.service .ico{width:72px;height:72px;border-radius:8px;background:var(--icon-bg);margin:0 auto 24px;display:flex;align-items:center;justify-content:center}

/* Remote sensing */
.remote{height:479px;background:linear-gradient(90deg,#1f6a78 0%,#2d7f86 40%,#6b7a6d 70%,#8a8a7e 100%)}
.remote .photo{position:absolute;inset:0}
.remote-copy{position:absolute;left:126px;top:178px;width:478px;color:var(--white)}
.remote h2{font-size:21px;font-weight:700}
.remote p{font-size:14.5px;line-height:19.5px;margin:28px 0 20px}
.play{position:absolute;left:805px;top:176px;width:112px;height:112px;border-radius:50%;background:rgba(255,255,255,.55);display:flex;align-items:center;justify-content:center}

/* Visual data */
.visual{height:553px;background:var(--grey);text-align:center}
.visual h2{padding-top:42px;font-size:20px;color:var(--ink)}
.visual .rule{margin-top:16px}
.visual .sub{font-size:14px;line-height:20px;margin-top:22px;color:var(--ink)}
.cards{position:absolute;top:178px;left:128px;display:flex;gap:19px;align-items:flex-start}
.card{width:302px;background:var(--white)}
.card .img{height:197px}
.card h3{font-size:14px;font-weight:700;color:var(--ink);padding:14px 0 12px}
.card.featured{background:var(--navy);height:315px}
.card.featured h3{color:var(--white)}
.card.featured p{color:var(--white);font-size:10px;line-height:14px;padding:0 36px}
.arrow{position:absolute;top:310px}

/* High tech */
.hightech{height:607px}
.frame{position:absolute;left:128px;top:59px;width:544px;height:480px;border:2px solid var(--navy)}
.frame-gap{position:absolute;left:664px;top:121px;width:12px;height:360px;background:var(--white)}
.hightech .img{position:absolute;left:152px;top:87px;width:434px;height:426px;background:linear-gradient(135deg,#cfe0f2 0%,#4f7fbf 35%,#1f4c94 60%,#c6a25a 100%)}
.hightech-copy{position:absolute;left:619px;top:160px;width:450px;color:var(--ink)}
.hightech h2{font-size:20px;font-weight:700}
.hightech .rule{margin:18px 0 36px}
.hightech p{font-size:14.5px;line-height:19.5px;margin-bottom:30px}

/* Partners */
.partners{height:194px;background:var(--light);text-align:center}
.partners h2{padding-top:34px;font-size:20px;color:var(--navy-dark)}
.partners .rule{margin-top:12px;width:110px}
.partner-row{position:absolute;top:114px;left:128px;width:944px;display:flex;justify-content:space-between;align-items:center}
.partner{height:30px;background:#b7c0cf;border-radius:4px}

/* Professionalism */
.excellence{height:475px;background:linear-gradient(180deg,#7fb2ec 0%,#a8cdf1 45%,#6f7f96 75%,#3c4a5e 100%);text-align:center}
.excellence h2{padding-top:44px;font-size:26px;font-weight:800;color:var(--navy)}
.excellence p{font-size:15px;line-height:22px;color:var(--ink);margin:10px 0 20px}

/* Footer */
.footer{height:286px;background:var(--navy-dark);color:var(--white)}
.footer .brand{position:absolute;left:128px;top:110px;font-size:34px}
.fcol{position:absolute;top:44px}
.fcol h4{font-family:"Montserrat",Arial,sans-serif;font-size:13.5px;font-weight:700;margin-bottom:8px}
.fcol p{font-size:14px;line-height:22px}
.fmenu a{display:block;font-size:11px;line-height:22px}
.social{display:flex;gap:14px;margin-top:6px}
.social span{width:34px;height:34px;border-radius:50%;background:var(--white)}
.footer .divider{position:absolute;left:128px;top:238px;width:942px;height:1px;background:rgba(255,255,255,.35)}
.copy{position:absolute;top:252px;width:100%;text-align:center;font-size:12px}
</style>
</head>
<body>

<header class="hero">
  <div role="img" aria-label="Aerial photograph of a city with a river and stadium" style="position:absolute;inset:0"></div>
  <div class="brand"><span>TERRAVIA</span><span class="brand-dot"></span></div>
  <nav class="nav">
    <a class="active">HOME</a><a>ABOUT</a><a>PRODUCTS</a><a>TECHNOLOGIES</a><a>WORK ETHOS</a><a>CONTACT</a>
    <span class="lang">EN <svg width="8" height="14" viewBox="0 0 8 14"><path d="M0 5h8L4 10z" fill="#fff"/></svg></span>
  </nav>
  <h1>WE INTEGRATE<br>EARTH &amp; SPACE DATA</h1>
  <p class="tag">FOR GOVERNMENTS, BUSINESS, INDUSTRY AND RESEARCH</p>
  <div class="dots"><span></span><span></span><span class="on"></span><span></span><span></span></div>
</header>

<section class="about">
  <div class="about-visual" role="img" aria-label="Spacecraft orbiting above Earth"></div>
  <div class="about-copy">
    <h2>ABOUT TERRAVIA</h2>
    <div class="line"></div>
    <p>Terravia B.V. is a company based in The Netherlands that provides specialized software for two important industries: Earth Observation technologies and High Tech Systems.</p>
    <p>Terravia provides you with the necessary support to develop your highly complex engineering products for your business. Our consulting services and our capacities provide you with the certainty that your efforts in engineering and R&amp;D will align with your objectives. We have a solid base in technical knowledge complemented with 20+ years of experience.</p>
    <p>We have developed products for academic and research institutions as well as commercial companies in the USA, Europe and Latin America. From medium sized business to large corporations, in local or regional contexts, we deliver your project in compliance with technical requirements, objectives and time frames.</p>
    <a class="btn">READ MORE</a>
  </div>
</section>

<section class="services">
  <h2>HIGH END SOFTWARE ENGINEERING</h2>
  <p class="sub">Built by expert software engineers, mathematicians, industry and field experts.</p>
  <div class="rule"></div>
  <div class="service-list">
    <div class="service"><div class="ico"><svg width="44" height="44" viewBox="0 0 44 44" fill="none" stroke="#2b4672" stroke-width="2"><circle cx="22" cy="22" r="16"/><circle cx="14" cy="16" r="2.5"/><circle cx="28" cy="14" r="2.5"/><circle cx="30" cy="27" r="2.5"/><circle cx="17" cy="29" r="2.5"/><path d="M14 16l14-2 2 13-13 2z"/></svg></div>Data Science &amp;<br>Artificial Intelligence</div>
    <div class="service"><div class="ico"><svg width="44" height="44" viewBox="0 0 44 44" fill="none" stroke="#2b4672" stroke-width="2"><path d="M12 24a7 7 0 0 1 2-14 9 9 0 0 1 17 2 6 6 0 0 1 0 12z"/><path d="M16 24v8M22 24v12M28 24v8"/><circle cx="16" cy="34" r="2"/><circle cx="22" cy="38" r="2"/><circle cx="28" cy="34" r="2"/></svg></div>Cloud<br>Computing</div>
    <div class="service"><div class="ico"><svg width="44" height="44" viewBox="0 0 44 44" fill="none" stroke="#2b4672" stroke-width="2.2"><rect x="8" y="26" width="6" height="12"/><rect x="19" y="20" width="6" height="18"/><rect x="30" y="14" width="6" height="24"/><path d="M8 20l10-8 8 4 10-9M31 7h5v5"/></svg></div>Mathematical /<br>Predictive Modeling</div>
    <div class="service"><div class="ico"><svg width="44" height="44" viewBox="0 0 44 44" fill="none" stroke="#2b4672" stroke-width="2.2"><rect x="6" y="9" width="32" height="22" rx="2"/><path d="M16 36h12M22 31v5M18 16l-4 4 4 4M26 16l4 4-4 4M23 15l-2 10"/></svg></div>Software Systems<br>Architecture</div>
  </div>
</section>

<section class="remote">
  <div class="photo" role="img" aria-label="Aerial view of a coastline meeting a town"></div>
  <div class="remote-copy">
    <h2>REMOTE SENSING FROM SPACE</h2>
    <p>Every day satellites sensing our planet deliver hundreds of gigabytes of data that are downloaded to Earth. If processed correctly this data finds commercial uses in industries such as finance, agriculture, logistics, security, disaster prevention and many others. However, transforming this raw data into decision-ready information requires expertise in mathematics, computing and science.</p>
    <a class="btn btn-light">READ MORE</a>
  </div>
  <div class="play"><svg width="40" height="46" viewBox="0 0 40 46"><path d="M4 2l34 21L4 44z" fill="#2b4672"/></svg></div>
</section>

<section class="visual">
  <h2>UNDERSTAND YOUR DATA VISUALLY</h2>
  <div class="rule"></div>
  <p class="sub">Our software pipeline is prepared to continually digest new input from space assets.<br>Additional data sources not only enhance dashboards, but are included in machine learning and predictive models.</p>
  <svg class="arrow" style="left:62px" width="22" height="36" viewBox="0 0 22 36"><path d="M18 4L5 18l13 14" fill="none" stroke="#9a9ca3" stroke-width="5"/></svg>
  <svg class="arrow" style="left:1116px" width="22" height="36" viewBox="0 0 22 36"><path d="M4 4l13 14L4 32" fill="none" stroke="#9a9ca3" stroke-width="5"/></svg>
  <div class="cards">
    <div class="card"><div class="img" role="img" aria-label="False-colour satellite image of a coastal region" style="background:linear-gradient(135deg,#5a9a3c 0%,#2a2f8a 45%,#7fa544 70%,#b07a4a 100%)"></div><h3>SPECIAL MONITORING</h3></div>
    <div class="card featured"><div class="img" role="img" aria-label="Radar imagery showing urban coverage" style="background:linear-gradient(180deg,#2b3d8c 0%,#4a9a2c 45%,#2a3a8a 100%)"></div><h3>SYNTHETIC APERTURE RADAR</h3><p>We offer our expertise in the ingestion and processing radar data. Here we monitor the evolution of urban coverage of San Salvador by analyzing signal coherence</p></div>
    <div class="card"><div class="img" role="img" aria-label="Black and white classification map of a valley" style="background:linear-gradient(135deg,#111 0%,#555 45%,#ccc 60%,#222 100%)"></div><h3>QUINOA IN PERU</h3></div>
  </div>
</section>

<section class="hightech">
  <div class="frame"></div>
  <div class="frame-gap"></div>
  <div class="img" role="img" aria-label="Blue-toned satellite image of a coastline and fields"></div>
  <div class="hightech-copy">
    <h2>HIGH TECH SYSTEMS</h2>
    <div class="rule"></div>
    <p>We work with several of the most sophisticated industries in the world that include aerospace, defense semiconductors, medical and big science. In close integration with our customers we design software components that comply with demanding requirements and proper software engineering practices. Our CI/CD procedure guarantees that quality: proper workload decomposition, rigorous issue tracking, well maintained source repositories, code reviews, automated building, packaging and testing.</p>
    <a class="btn">READ MORE</a>
  </div>
</section>

<section class="partners">
  <h2>PARTNERS</h2>
  <div class="rule"></div>
  <svg style="position:absolute;left:66px;top:118px" width="16" height="26" viewBox="0 0 16 26"><path d="M13 3L4 13l9 10" fill="none" stroke="#9a9ca3" stroke-width="4"/></svg>
  <svg style="position:absolute;left:1100px;top:118px" width="16" height="26" viewBox="0 0 16 26"><path d="M3 3l9 10-9 10" fill="none" stroke="#9a9ca3" stroke-width="4"/></svg>
  <div class="partner-row">
    <span class="partner" style="width:150px"></span>
    <span class="partner" style="width:66px"></span>
    <span class="partner" style="width:98px"></span>
    <span class="partner" style="width:130px"></span>
    <span class="partner" style="width:136px"></span>
    <span class="partner" style="width:130px"></span>
  </div>
</section>

<section class="excellence">
  <div role="img" aria-label="Fisheye aerial view of a city skyline under blue sky" style="position:absolute;inset:0"></div>
  <h2>PROFESSIONALISM AND EXCELLENCE</h2>
  <p>Organization and order are important factors for the delivery of successful<br>projects and the creation of high impact products.</p>
  <a class="btn">READ MORE</a>
</section>

<footer class="footer">
  <div class="brand"><span>TERRAVIA</span><span class="brand-dot"></span></div>
  <div class="fcol" style="left:420px">
    <h4>ADDRESS</h4>
    <p>Lindenhofstraat 18,<br>Delft, The Netherlands</p>
    <h4 style="margin-top:24px">EMAIL US</h4>
    <p>hello@terravia.example</p>
  </div>
  <div class="fcol fmenu" style="left:722px">
    <h4>MENU</h4>
    <a>ABOUT</a><a>PRODUCTS</a><a>TECHNOLOGIES</a><a>WORK ETHOS</a><a>CONTACT</a>
  </div>
  <div class="fcol" style="left:912px">
    <h4>BE SOCIAL WITH US</h4>
    <div class="social"><span></span><span></span><span></span></div>
  </div>
  <div class="divider"></div>
  <p class="copy">© 2022 Terravia. All Rights Reserved.</p>
</footer>

</body>
</html>
```